Lantern Square, Steady Course. (Website Design)

We are launching a new bipartisan civic movement: Lantern Square. Steady Course.
The mission is this: Americans deserve a government that is legally required to serve them honestly.
We are looking for a world-class website designer capable of creating an emotionally powerful, modern, cinematic landing page experience that feels larger than politics.
This is not a campaign website for a political party or candidate. We are not looking for a red, white, and blue page with stripes, or American flags, or stock footage of smiling people in a voting booth. We are looking for an emotional and cinematic experience through and through.
The visual direction should feel:
Historic
Hopeful
American
Emotional
Cinematic
Trustworthy
Timeless
The goal is to make visitors feel that they are witnessing the beginning of something important and want to be part of it in the end.
Primary Objective:
Inspire visitors to participate in a one-minute survey and cast their vote.
The survey itself is extremely short and takes approximately one minute to complete.
Everything on the page should ultimately guide visitors toward this action while creating enough curiosity, trust, emotional engagement, and excitement that they feel compelled to take part in the movement.
Audience:
The audience is ordinary Americans across the political spectrum: Democrats, Republicans, Independents.
The design should feel unifying and welcoming.
It should avoid looking partisan, ideological, activist, or government-issued.
Creative Freedom:
We are intentionally giving designers substantial creative freedom.
We are not looking for someone to simply arrange content into predefined sections.
Instead, we are looking for a designer who can think strategically about user experience and persuasion.
The ideal design is as minimal as possible, but you may always:
Use as many sections as you believe are necessary.
Use as many images as you believe are necessary.
Include storytelling elements.
Include data visualizations.
Include timelines.
Include videos.
Include animations.
Include or exclude sections as you see fit.
Reorganize the flow entirely.
We uploaded some files containing text and section suggestions. You don’t have to use them.
We also uploaded some images to convey the general feel we’re looking for.
We are much more interested in the effectiveness of the overall experience than in any specific layout.
What success looks like:
Think outside the box.
Please do not create another generic political website. We have already explored those approaches.
We are looking for something different.
The winning design will be the one that most effectively guides visitors from curiosity to belief to participation.
When a visitor reaches the end of the experience, they should feel:
This is bigger than politics.
This is something I can support regardless of party.
This feels credible.
This feels hopeful.
I want to be part of this.
Use the survey results, the research findings, the principles, the storytelling, or any other elements you believe will help build trust and inspire participation.
Don't just impress us with flashy visuals. Impress us with a website experience that inspires people to become part of the movement and cast their vote.
The final call-to-action should feel like the natural conclusion of the journey, not a request for engagement.
Our goal is not simply to inform visitors. Our goal is to inspire them to cast their vote.
Prioritize emotional impact, storytelling, clarity, and persuasion over decorative design elements.
Final words:
Design a website experience that successfully inspires visitors to take the survey and cast their vote.
Think like a storyteller, not just a designer.
Thank you for your interest in the project.
Best of luck.

```html
<!DOCTYPE html>
<html lang="en">
<head>
<meta charset="utf-8">
<title>Lantern Square, Steady Course.</title>
<link rel="stylesheet" href="https://fonts.googleapis.com/css2?family=Outfit:wght@400;500;600;700&family=Poppins:wght@400;500;600&family=Oswald:wght@500;600&display=swap">
<style>
:root{
  --red:#d01212;
  --red-dark:#b50d0d;
  --navy:#121f5c;
  --navy-deep:#0b1442;
  --ink:#15161c;
  --muted:#3d3f4a;
  --paper:#eef2f5;
  --panel:#e6ebf0;
  --steel:#c9d6df;
  --white:#ffffff;
  --stat:#1c2c74;
}
*{box-sizing:border-box;margin:0;padding:0}
html,body{width:1200px;height:3805px;overflow:hidden}
body{font-family:"Poppins",sans-serif;color:var(--ink);background:var(--paper);position:relative}
section,header,footer{position:relative;width:1200px;overflow:hidden}
.abs{position:absolute}
.display{font-family:"Outfit",sans-serif}
.condensed{font-family:"Oswald",sans-serif}

/* hero */
.hero{height:661px;background:#2a2018}
.hero-photo{position:absolute;inset:0;background:
  radial-gradient(ellipse 420px 300px at 560px 330px,rgba(255,196,96,.85),rgba(214,120,40,.4) 55%,transparent 80%),
  radial-gradient(ellipse 300px 380px at 290px 240px,rgba(120,96,80,.55),transparent 75%),
  radial-gradient(ellipse 260px 300px at 1000px 260px,rgba(200,150,120,.45),transparent 75%),
  linear-gradient(180deg,#2c2b30 0%,#5a4030 40%,#6e3a24 70%,#2a1e1c 100%)}
.hero-shade{position:absolute;inset:0;background:linear-gradient(180deg,rgba(0,0,0,.35) 0%,transparent 20%,transparent 60%,rgba(0,0,0,.35) 100%)}
.brand{font-family:"Poppins",sans-serif;font-size:15px;line-height:17px;font-weight:400;text-transform:uppercase;color:var(--white);letter-spacing:.2px}
.nav a{position:absolute;top:29px;font-size:12px;letter-spacing:.8px;color:var(--white);text-decoration:none;font-weight:500}
.nav .vote{top:22px;left:931px;width:98px;height:31px;background:var(--red);text-align:center;line-height:31px;font-weight:400}
.hero h1{left:173px;top:462px;font-family:"Outfit",sans-serif;font-weight:700;font-size:45px;line-height:53px;color:var(--white)}
.watch{left:173px;top:592px;display:flex;align-items:center;gap:14px;color:var(--white);font-size:11px;letter-spacing:2px;text-transform:uppercase}
.watch span{width:36px;height:36px;border:2px solid var(--white);border-radius:50%;display:flex;align-items:center;justify-content:center}

/* mission */
.mission{height:307px;background:var(--paper);text-align:center}
.mission .label{top:59px;width:100%;font-size:11px;letter-spacing:.6px;color:var(--navy);text-transform:uppercase}
.mission .lead{top:88px;width:100%;font-family:"Outfit",sans-serif;font-weight:600;font-size:20px;line-height:29px}
.mission .question{top:157px;width:100%;font-size:16.5px;line-height:28px;color:var(--muted)}
.mission .note{top:226px;width:100%;font-size:12px;color:var(--muted)}

/* who we are */
.who{height:441px;background:var(--red);color:var(--white)}
.who h2{left:171px;top:68px;font-family:"Outfit",sans-serif;font-weight:600;font-size:33px;letter-spacing:.4px}
.who .sub{left:171px;top:118px;width:400px;font-size:19px;line-height:30px}
.who .body{left:171px;top:193px;width:380px;font-size:12.5px;line-height:20.5px}
.who .body p+p{margin-top:12px}
.tile{position:absolute}

/* journey */
.journey{height:830px;background:var(--paper)}
.journey h2{width:100%;text-align:center;top:52px;font-family:"Outfit",sans-serif;font-weight:600;font-size:35px;letter-spacing:.5px}
.spine{left:599px;top:172px;width:2px;height:550px;background:var(--navy)}
.step{position:absolute;width:62px;height:62px;border-radius:50%;background:var(--white);border:2px solid var(--navy);left:569px;display:flex;align-items:center;justify-content:center}
.step.final{background:var(--red);border-color:var(--navy)}
.date{position:absolute;font-family:"Oswald",sans-serif;font-weight:600;font-size:45px;line-height:50px;color:var(--red);letter-spacing:-.5px}
.rule{position:absolute;height:1px;background:#b5bcc7}
.step-text{position:absolute;font-size:12.5px;line-height:21px;color:var(--muted);width:290px}
.step-text.left{text-align:right}

/* principles */
.principles{height:522px;background:
  radial-gradient(ellipse 700px 260px at 600px 330px,rgba(58,82,170,.55),transparent 75%),
  linear-gradient(180deg,#141c57 0%,#17246a 55%,#1a3790 100%);color:var(--white)}
.principles h2{width:100%;text-align:center;top:52px;font-family:"Outfit",sans-serif;font-weight:600;font-size:38px;letter-spacing:.4px}
.card{position:absolute;width:204px;height:144px;border:1px solid rgba(255,255,255,.2);background:rgba(255,255,255,.03);text-align:center;font-size:12.5px;line-height:18.5px;padding:30px 16px 0}
.num{position:absolute;top:-14px;left:88px;width:28px;height:28px;border-radius:50%;background:var(--red);font-size:14px;line-height:28px;font-weight:500}
.card.stat{padding-top:32px}
.card.stat b{display:block;font-family:"Oswald",sans-serif;font-weight:500;font-size:44px;line-height:52px}

/* survey */
.survey{height:528px;background:var(--white)}
.survey h2{left:171px;top:74px;font-family:"Outfit",sans-serif;font-weight:700;font-size:36px;line-height:37px}
.pct{font-family:"Oswald",sans-serif;font-weight:500;color:var(--stat)}
.survey .intro-stat{left:389px;top:58px;font-size:22px;color:var(--ink)}
.survey .intro-text{left:389px;top:101px;width:185px;font-size:12.5px;line-height:19px;color:var(--muted)}
.survey .divider{left:578px;top:102px;width:1px;height:36px;background:#c9ced6}
.survey .intro-right{left:597px;top:101px;width:420px;font-size:12.5px;line-height:19px;color:var(--muted)}
.survey-panel{left:171px;top:164px;width:858px;height:300px;background:var(--panel);border-radius:8px}
.scard{position:absolute;background:var(--white);border-radius:6px;font-size:12px;line-height:17px;color:var(--muted)}
.scard .pct{font-size:19px;line-height:22px}
.scard strong{color:var(--ink);font-weight:600}
.ticks li{list-style:none;position:relative;padding-left:14px;margin-bottom:3px}
.ticks li::before{content:"";position:absolute;left:1px;top:4px;width:4px;height:8px;border:solid var(--red);border-width:0 2px 2px 0;transform:rotate(45deg)}

/* cta */
.cta{height:369px;color:var(--white)}
.cta-photo{position:absolute;inset:0;background:
  radial-gradient(ellipse 380px 240px at 880px 170px,rgba(70,120,220,.75),transparent 75%),
  linear-gradient(180deg,#112160 0%,#17307e 55%,#0f1f5a 100%)}
.cta h2{left:171px;top:58px;font-family:"Outfit",sans-serif;font-weight:600;font-size:36px;letter-spacing:.2px}
.cta .copy{left:171px;top:112px;width:470px;font-size:12.5px;line-height:17.5px}
.cta .copy p+p{margin-top:17px}
.btn{left:171px;top:264px;width:182px;height:34px;background:var(--red);color:var(--white);font-size:11px;font-weight:500;letter-spacing:.3px;display:flex;align-items:center;justify-content:center;gap:8px;text-transform:uppercase}
.counter{left:788px;top:82px;width:233px;height:204px;border:1px solid rgba(160,190,255,.5);border-radius:6px;background:rgba(40,80,170,.55);text-align:center}
.counter .icon{position:absolute;left:95px;top:22px;width:42px;height:42px;border-radius:50%;background:var(--red);display:flex;align-items:center;justify-content:center}
.counter b{position:absolute;top:74px;width:100%;font-family:"Outfit",sans-serif;font-weight:500;font-size:38px}
.counter p{position:absolute;top:128px;width:100%;font-size:12.5px;line-height:17.5px}

/* footer */
.site-footer{height:147px;background:var(--white)}
.site-footer .brand{color:var(--navy);left:173px;top:22px}
.foot-nav a{position:absolute;top:41px;font-size:12px;color:var(--ink);text-decoration:none;letter-spacing:.3px}
.social{position:absolute;top:38px;display:flex;align-items:center;gap:7px;font-size:12.5px;color:var(--ink)}
.social i{width:11px;height:11px;border-radius:50%;border:1.5px solid var(--navy)}
.copyright{position:absolute;top:114px;width:100%;text-align:center;font-size:11.5px;color:var(--muted)}
.footline{position:absolute;left:0;top:100px;width:1200px;height:1px;background:#e3e6ea}
</style>
</head>
<body>

<header class="hero">
  <div class="hero-photo" role="img" aria-label="Warm cinematic montage of a historic president's portrait, a waving flag and a smiling young woman at sunset"></div>
  <div class="hero-shade"></div>
  <div class="abs brand" style="left:173px;top:15px">Lantern<br>Square<br>Steady Course</div>
  <nav class="nav">
    <a style="left:531px">MISSION</a>
    <a style="left:627px">JOURNEY</a>
    <a style="left:729px">PRINCIPLES</a>
    <a style="left:842px">SURVEY</a>
    <a class="vote">VOTE NOW</a>
  </nav>
  <h1 class="abs">A Government That Serves<br>The People Honestly</h1>
  <div class="abs watch"><span><svg width="12" height="13" viewBox="0 0 12 13"><path d="M2 1l9 5.5L2 12z" fill="#fff"/></svg></span>Watch the video</div>
</header>

<section class="mission">
  <p class="abs label">Mission Statement</p>
  <p class="abs lead">Today, not a single law binds our government<br>to act honestly, and in our best interest.</p>
  <p class="abs question">If our government exists solely to serve us,<br>Why isn’t it legally required to?</p>
  <p class="abs note">We founded this movement to change that.</p>
</section>

<section class="who">
  <svg class="abs" style="left:0;top:0" width="1200" height="441" aria-hidden="true">
    <polygon points="640,0 1095,0 910,441 445,441" fill="#e9eef2"/>
    <polygon points="1060,0 1095,0 910,441 875,441" fill="#c3d1dc"/>
    <polygon points="600,70 650,70 490,441 440,441" fill="#c3d1dc"/>
  </svg>
  <h2 class="abs">WHO WE ARE</h2>
  <p class="abs sub">We are a bipartisan movement based in Washington, D.C.</p>
  <div class="abs body">
    <p>We believe Americans deserve a government legally required to act honestly, transparently, and in the public’s best interest.</p>
    <p>At a time of growing division and distrust, we are working to unite Americans around a simple idea: government should faithfully serve the people, not special interests.</p>
  </div>
  <div class="tile" style="left:659px;top:19px;width:120px;height:121px;background:linear-gradient(135deg,#6b6b6b,#1f1f1f)" role="img" aria-label="Black and white photo of a civil rights leader speaking at a microphone"></div>
  <div class="tile" style="left:786px;top:19px;width:123px;height:121px;background:linear-gradient(135deg,#c79a4a,#5a3a1a)" role="img" aria-label="Sepia portrait photo of a civil rights leader"></div>
  <div class="tile" style="left:916px;top:19px;width:113px;height:121px;background:linear-gradient(135deg,#9a9a9a,#2e2e2e)" role="img" aria-label="Black and white portrait photo of a civil rights activist"></div>
  <div class="tile" style="left:559px;top:149px;width:128px;height:148px;background:linear-gradient(135deg,#7d8ca0,#2d3442)" role="img" aria-label="Photo of a president delivering a speech"></div>
  <div class="tile" style="left:695px;top:149px;width:174px;height:148px;background:linear-gradient(135deg,#4a4f5c,#15171d)" role="img" aria-label="Photo of marchers holding signs for jobs and freedom"></div>
  <div class="tile" style="left:876px;top:149px;width:128px;height:148px;background:linear-gradient(135deg,#b9ab8c,#5d5240)" role="img" aria-label="Photo of a bootprint on the lunar surface"></div>
  <div class="tile" style="left:538px;top:305px;width:105px;height:116px;background:linear-gradient(135deg,#b4a08a,#4a3e33)" role="img" aria-label="Photo of the Capitol dome beside a statue"></div>
  <div class="tile" style="left:650px;top:305px;width:119px;height:116px;background:linear-gradient(135deg,#8a7a6a,#2a241f)" role="img" aria-label="Photo of a leader waving to a crowd on the National Mall"></div>
  <div class="tile" style="left:777px;top:305px;width:110px;height:116px;background:linear-gradient(135deg,#a8564a,#3a2622)" role="img" aria-label="Photo of a historic march with protest banners"></div>
</section>

<section class="journey">
  <h2 class="abs">OUR JOURNEY</h2>
  <div class="abs spine"></div>

  <div class="step" style="top:141px"><svg width="26" height="26" viewBox="0 0 26 26" fill="none" stroke="#d01212" stroke-width="1.5"><path d="M9 15a6 6 0 1 1 8 0c-1 1-1.5 2-1.5 3h-5c0-1-.5-2-1.5-3z"/><path d="M10.5 21h5M11 23.5h4M13 2v-1M4 5l-1-1M22 5l1-1"/></svg></div>
  <div class="rule" style="left:631px;top:171px;width:285px"></div>
  <div class="date" style="left:656px;top:119px">AUGUST 2024</div>
  <p class="step-text" style="left:656px;top:181px">We turned those principles into a rigorous framework and named it Lantern Square, Steady Course.</p>

  <div class="step" style="top:278px"><svg width="26" height="26" viewBox="0 0 26 26" fill="none" stroke="#d01212" stroke-width="1.8"><circle cx="11" cy="11" r="7"/><path d="M16 16l6 6"/></svg></div>
  <div class="rule" style="left:290px;top:308px;width:279px"></div>
  <div class="date" style="right:656px;top:256px;text-align:right">OCTOBER 2025</div>
  <p class="step-text left" style="left:254px;top:318px">We identified 10 principles that most of Americans agree our government must uphold.</p>

  <div class="step" style="top:416px"><svg width="24" height="26" viewBox="0 0 24 26" fill="none" stroke="#d01212" stroke-width="1.5"><path d="M4 2h11l5 5v17H4z"/><path d="M8 11h8M8 15h8M8 19h6"/></svg></div>
  <div class="rule" style="left:631px;top:446px;width:285px"></div>
  <div class="date" style="left:656px;top:394px">MARCH 2026</div>
  <p class="step-text" style="left:656px;top:455px">We turned those principles into a rigorous framework and named it Lantern Square, Steady Course.</p>

  <div class="step" style="top:554px"><svg width="26" height="26" viewBox="0 0 26 26" fill="none" stroke="#d01212" stroke-width="1.5"><rect x="5" y="4" width="16" height="19" rx="2"/><path d="M10 2h6v4h-6z"/><path d="M9 12l2 2 3-3M9 18h8"/></svg></div>
  <div class="rule" style="left:290px;top:584px;width:279px"></div>
  <div class="date" style="right:656px;top:532px;text-align:right">APRIL 2026</div>
  <p class="step-text left" style="left:254px;top:593px">We tested the framework in a pre-registered national study with Americans across the political spectrum.</p>

  <div class="step final" style="top:691px"><svg width="28" height="24" viewBox="0 0 28 24" fill="none" stroke="#fff" stroke-width="1.5"><rect x="2" y="3" width="24" height="17"/><path d="M6 16v-4M10 16v-7M14 16v-5M18 16v-8M22 16v-3M6 10l4-3 4 2 4-4 4 3"/></svg></div>
  <p class="step-text" style="left:656px;top:700px;width:240px">And the results exceeded all our expectation.</p>
</section>

<section class="principles">
  <h2 class="abs">THE SEVEN PRINCIPLES</h2>
  <div class="card" style="left:171px;top:138px"><span class="num">1</span>Public officials should only serve the public good. Not private interests.</div>
  <div class="card" style="left:389px;top:138px"><span class="num">2</span>Major government decisions should be based on truth, and rigorous evidence. Not party loyalty, pressure, or donors.</div>
  <div class="card" style="left:607px;top:138px"><span class="num">3</span>When a public decision is made, people should be able to see the reasoning. Clearly. Honestly. On the record.</div>
  <div class="card" style="left:825px;top:138px"><span class="num">4</span>And if the government reasoning is flawed, citizens should have a way to challenge it, And get a real response.</div>
  <div class="card" style="left:171px;top:316px"><span class="num">5</span>Conflicts of interest in public office all should be disclosed, Before decisions are made.</div>
  <div class="card" style="left:389px;top:316px"><span class="num">6</span>Lying or misleading the public in official decisions should carry consequences. Real ones.</div>
  <div class="card" style="left:607px;top:316px"><span class="num">7</span>And most importantly, Money should never outweigh people’s voice.</div>
  <div class="card stat" style="left:825px;top:316px"><b>89.9%*</b>Said Agree.</div>
</section>

<section class="survey">
  <h2 class="abs">THE<br>SURVEY</h2>
  <div class="abs intro-stat pct">82.9%*</div>
  <p class="abs intro-text">of Americans said YES on a state ballot vote.</p>
  <div class="abs divider"></div>
  <p class="abs intro-right">We conducted a pre-registered national study with X number Americans across the political spectrum.</p>

  <div class="abs survey-panel">
    <div class="scard" style="left:19px;top:18px;width:370px;height:99px">
      <svg class="abs" style="left:20px;top:36px" width="22" height="26" viewBox="0 0 22 26" fill="none" stroke="#d01212" stroke-width="1.5"><rect x="2" y="3" width="18" height="21" rx="2"/><path d="M7 1h8v4H7zM6 11l1.5 1.5L10 10M12 11h5M6 17l1.5 1.5L10 16M12 17h5"/></svg>
      <p class="abs" style="left:56px;top:24px;width:175px">We first laid out the 7 principles. We asked if they agree?</p>
      <div class="abs" style="left:239px;top:26px;width:1px;height:44px;background:#d4d8de"></div>
      <div class="abs" style="left:250px;top:26px"><div class="pct">89.9%*</div><div style="color:var(--stat)">Said Agree.</div></div>
    </div>
    <div class="scard" style="left:19px;top:122px;width:370px;height:161px">
      <p class="abs" style="left:20px;top:18px;width:320px"><strong>Then we asked:</strong><br>Would you support a legal framework built around them?</p>
      <div class="abs" style="left:20px;top:101px"><div class="pct">82.9%*</div>Said yes.</div>
      <div class="abs" style="left:106px;top:101px"><div class="pct">14.4%*</div>Remained neutral.</div>
      <div class="abs" style="left:236px;top:85px">Only<div class="pct">82.9%*</div>Actively opposed it.</div>
    </div>
    <div class="scard" style="left:398px;top:18px;width:284px;height:265px">
      <svg class="abs" style="left:18px;top:20px" width="28" height="26" viewBox="0 0 28 26" fill="none" stroke="#d01212" stroke-width="1.5"><path d="M14 3v20M8 23h12M4 7h20M4 7l-3 8h6zM24 7l-3 8h6zM1 15a3 3 0 0 0 6 0M21 15a3 3 0 0 0 6 0"/></svg>
      <p class="abs" style="left:60px;top:20px;width:205px"><strong>But broad support is easy when ideas stay vague. So we stress-tested it.</strong></p>
      <p class="abs" style="left:60px;top:74px;width:205px">We showed participants the full framework.</p>
      <ul class="abs ticks" style="left:18px;top:128px">
        <li>The legal structure.</li>
        <li>The enforcement model.</li>
        <li>The actual mechanism.</li>
      </ul>
      <p class="abs" style="left:18px;top:212px;width:250px">Most reforms lose support once the details appear. This one didn’t. Support held.</p>
    </div>
    <div class="scard" style="left:691px;top:18px;width:147px;height:265px">
      <svg class="abs" style="left:18px;top:18px" width="32" height="30" viewBox="0 0 32 30" fill="none" stroke="#d01212" stroke-width="1.5"><circle cx="11" cy="9" r="6"/><path d="M1 28c0-6 4-10 10-10s10 4 10 10z"/><circle cx="22" cy="11" r="5"/><path d="M23 19c5 0 8 3 8 9h-8"/></svg>
      <div class="abs" style="left:18px;top:73px">Democrats<div class="pct">84.5%*</div></div>
      <div class="abs" style="left:18px;top:127px">Republicans<div class="pct">80.2%*</div></div>
      <div class="abs" style="left:18px;top:181px">Independants<div class="pct">79.9%*</div></div>
      <p class="abs" style="left:18px;top:238px">They all said, YES.</p>
    </div>
  </div>
</section>

<section class="cta">
  <div class="cta-photo" role="img" aria-label="Aerial view of a vast crowd of people gathering in a deep blue light"></div>
  <h2 class="abs">BE PART OF HISTORY. VOTE NOW.</h2>
  <div class="abs copy">
    <p>For decades, we have argued over policies, parties, and ideologies.<br>But today, across political lines, generations, and races,<br>Americans are arriving at the same conclusion:</p>
    <p>We deserve a government legally required to serve the people honestly.</p>
    <p>And we don’t have to ask for it. We just have to vote for it.</p>
  </div>
  <div class="abs btn">Cast your vote now <svg width="12" height="10" viewBox="0 0 12 10" fill="none" stroke="#fff" stroke-width="1.5"><path d="M0 5h10M6 1l4 4-4 4"/></svg></div>
  <div class="abs counter">
    <div class="icon"><svg width="24" height="18" viewBox="0 0 24 18" fill="none" stroke="#fff" stroke-width="1.4"><circle cx="12" cy="5" r="3"/><circle cx="5" cy="6" r="2.5"/><circle cx="19" cy="6" r="2.5"/><path d="M6 17c0-4 3-6 6-6s6 2 6 6zM1 15c0-3 2-5 4-5M23 15c0-3-2-5-4-5"/></svg></div>
    <b>1016</b>
    <p>People<br>Already Voted YES for<br>the Ballot</p>
  </div>
</section>

<footer class="site-footer">
  <div class="abs brand">Lantern<br>Square<br>Steady Course</div>
  <nav class="foot-nav">
    <a style="left:355px">MISSION</a>
    <a style="left:439px">JOURNEY</a>
    <a style="left:528px">PRINCIPLES</a>
    <a style="left:627px">SURVEY</a>
    <a style="left:705px">VOTE NOW</a>
  </nav>
  <div class="social" style="left:843px"><i></i>Townboard</div>
  <div class="social" style="left:942px"><i></i>Picturepost</div>
  <div class="footline"></div>
  <p class="copyright">© Copyright 2026 Lantern Square Steady Course. All Rights Reserved</p>
</footer>

</body>
</html>
```